KELPMARROW, LLC needs a hybrid app to evaluate and develop athletes

KELPMARROW, LLC needs initial hybrid mobile app and website holding page. KELPMARROW, LLC allows athletes to develop their skills (soccer is initial sport) for free. Receive daily/weekly reminders. Access training videos. Earn points to "upgrade" their soccer profile in "app soccer store". See their points/rankings compared to all app users. Progress streak. This free app (for athletes) will communicate to paid app (coaches) in the future. We would like to see designs use the color blue. The design will communicate health and wellness.

```html
<!DOCTYPE html>
<html lang="en">
<head>
<meta charset="utf-8">
<title>KELPMARROW, LLC – App Screens</title>
<link href="https://fonts.googleapis.com/css2?family=Oswald:wght@700&family=Roboto:wght@300;400;700&family=Roboto+Condensed:wght@700&display=swap" rel="stylesheet">
<style>
  :root{
    --stage:#6b6b6b;
    --blue-deep:#0d4fa8;
    --blue-mid:#1f6fd1;
    --blue-light:#5aaeff;
    --ink:#222;
    --muted:#8a8f96;
    --line:#d5d9de;
    --dark-btn:#4a4a4a;
    --white:#fff;
    --gold:#f2cf4a;
    --green:#2f9a45;
    --teal:#5cc6d8;
    --violet:#7366c9;
    --ball-grey:#c9cbcf;
  }
  *{box-sizing:border-box;margin:0;padding:0}
  html,body{width:1200px;height:590px;overflow:hidden;background:var(--stage)}
  body{position:relative;font-family:"Roboto",sans-serif}

  .screen{position:absolute;top:63px;width:224px;height:464px;border-radius:24px;overflow:hidden;background:var(--white)}
  .screen--splash{left:80px;background:linear-gradient(160deg,#4f9ff0 0%,var(--blue-mid) 45%,#3a95f2 75%,#7cc2ff 100%)}
  .screen--login{left:354px}
  .screen--signup{left:627px}
  .screen--challenge{left:900px}

  .wordmark{font-family:"Oswald",sans-serif;font-weight:700;color:var(--white);text-align:center;letter-spacing:-.5px;line-height:1}

  /* splash */
  .status{position:absolute;top:9px;left:18px;right:20px;display:flex;justify-content:space-between;color:var(--white);font-size:8px}
  .status__icons{display:flex;gap:5px;align-items:center}
  .splash__wordmark{position:absolute;top:70px;left:0;right:0;font-size:30px}
  .splash__art{position:absolute;left:10px;right:0;top:225px;bottom:35px;border-radius:40% 30% 20% 30%;background:radial-gradient(ellipse at 35% 55%,rgba(255,210,190,.45),rgba(140,195,255,.35) 45%,rgba(30,90,170,0) 75%)}

  /* header band */
  .band{position:absolute;top:0;left:0;width:224px;height:120px}
  .band__wordmark{position:absolute;left:0;right:0;font-size:25px}
  .band__sub{position:absolute;left:0;right:0;text-align:center;color:var(--white);font-size:11px;font-weight:300;letter-spacing:.2px}
  .band__sub b{font-weight:700}
  .band__rule{position:absolute;left:97px;width:30px;height:1.5px;background:var(--white)}

  /* login */
  .avatar{position:absolute;left:59px;top:115px;width:98px;height:98px;border-radius:50%;border:2px solid var(--blue-deep);background:radial-gradient(circle at 50% 40%,#d9a98a 0%,#8a7a5a 40%,#3f6a3a 70%,#2a3a2a 100%)}
  .login__title{position:absolute;top:221px;left:0;right:0;text-align:center;font-size:21px;font-weight:300;letter-spacing:1.5px;color:var(--blue-deep)}
  .login__title b{font-weight:700}

  .field{position:absolute;left:15px;width:195px;height:28px;border:1px solid var(--line);border-radius:2px;background:var(--white);display:flex;align-items:center;justify-content:space-between;padding:0 8px;color:var(--muted);font-size:11.5px;font-weight:300}
  .field svg{width:16px;height:16px;stroke:var(--muted);fill:none;stroke-width:1.1}
  .btn{position:absolute;left:15px;width:195px;height:32px;border-radius:2px;display:flex;align-items:center;justify-content:center;gap:8px;color:var(--white);font-family:"Roboto Condensed",sans-serif;font-weight:700;font-size:12.5px;letter-spacing:.3px}
  .btn svg{width:16px;height:16px;stroke:var(--white);fill:none;stroke-width:1.3}
  .btn--dark{background:var(--dark-btn)}
  .btn--blue{background:var(--blue-deep)}

  .footer{position:absolute;left:0;right:0;bottom:0;height:26px;border-top:1px solid #e4e6e9;display:flex;align-items:center;justify-content:space-around;font-size:5.3px;font-weight:700;color:var(--ink)}
  .footer span+span{border-left:1px solid #e4e6e9;padding-left:6px}

  /* challenge */
  .badge{position:absolute;left:80px;top:88px;width:64px;height:64px;border-radius:50%;background:var(--white);border:3px solid var(--blue-deep);box-shadow:0 0 0 2px var(--white)}
  .badge::after{content:"";position:absolute;inset:18px;background:var(--blue-deep);clip-path:polygon(50% 0,100% 38%,82% 100%,18% 100%,0 38%)}
  .week{position:absolute;width:52px;text-align:center;font-size:9px;font-weight:700;color:var(--blue-deep)}
  .week__ball{display:block;margin:0 auto 4px;width:40px;height:40px;border-radius:50%;border:2px solid #9a9da2;background:radial-gradient(circle,#fff 30%,var(--ball-grey) 31%,var(--ball-grey) 40%,#fff 41%)}
  .week__ball--green{border:3px solid var(--gold);background:radial-gradient(circle,#fff 28%,var(--green) 29%,var(--green) 42%,#fff 43%,#fff 55%,var(--green) 56%)}
  .week__ball--teal{border:3px solid var(--gold);background:radial-gradient(circle,#fff 28%,var(--teal) 29%,var(--teal) 42%,#fff 43%,#fff 55%,var(--teal) 56%)}
  .week__ball--violet{border:3px solid var(--gold);background:radial-gradient(circle,#fff 28%,var(--violet) 29%,var(--violet) 42%,#fff 43%,#fff 55%,var(--violet) 56%)}
  .tabbar{position:absolute;left:0;right:0;bottom:0;height:38px;border-top:1px solid #e4e6e9;display:flex;background:var(--white)}
  .tabbar__item{flex:1;display:flex;align-items:center;justify-content:center}
  .tabbar__item+.tabbar__item{border-left:1px solid #e4e6e9}
  .tabbar svg{width:30px;height:26px}
</style>
</head>
<body>

<!-- Splash -->
<section class="screen screen--splash">
  <div class="status">
    <div class="status__icons">
      <svg width="9" height="6" viewBox="0 0 9 6" fill="#fff"><rect x="0" y="4" width="1.3" height="2"/><rect x="2.4" y="3" width="1.3" height="3"/><rect x="4.8" y="1.5" width="1.3" height="4.5"/><rect x="7.2" y="0" width="1.3" height="6"/></svg>
      <svg width="14" height="6" viewBox="0 0 14 6"><rect x=".5" y=".5" width="12" height="5" rx="1.5" fill="none" stroke="#fff"/><rect x="2" y="2" width="9" height="2" fill="#fff"/></svg>
    </div>
    <span>12:29</span>
  </div>
  <h1 class="wordmark splash__wordmark">KELPMARROW LLC</h1>
  <div class="splash__art" role="img" aria-label="Network-style illustration of a running soccer player"></div>
</section>

<!-- Athlete login -->
<section class="screen screen--login">
  <svg class="band" viewBox="0 0 224 120" preserveAspectRatio="none">
    <defs><linearGradient id="bandA" x1="0" y1="0" x2="1" y2="1"><stop offset="0" stop-color="#4c9df0"/><stop offset=".6" stop-color="#1560c4"/><stop offset="1" stop-color="#0d4fa8"/></linearGradient></defs>
    <polygon points="0,0 224,0 224,84 144,104 0,72" fill="url(#bandA)"/>
    <polygon points="144,104 224,84 224,90" fill="#b8bcc2"/>
  </svg>
  <h1 class="wordmark band__wordmark" style="top:38px">KELPMARROW LLC</h1>
  <div class="avatar" role="img" aria-label="Athlete profile photo"></div>
  <h2 class="login__title">ATHLETE <b>LOGIN</b></h2>
  <div class="field" style="top:248px">Username:
    <svg viewBox="0 0 16 16"><circle cx="8" cy="8" r="7"/><circle cx="8" cy="6.5" r="2.5"/><path d="M3.5 13c1-2.5 3-3 4.5-3s3.5.5 4.5 3"/></svg></div>
  <div class="field" style="top:283px">Pasword:
    <svg viewBox="0 0 16 16"><circle cx="11" cy="5" r="3.5"/><path d="M8.5 7.5 2 14M4 12l1.5 1.5M5.5 10.5 7 12"/></svg></div>
  <div class="btn btn--dark" style="top:317px">SIGN IN
    <svg viewBox="0 0 16 16"><rect x="4" y="1" width="8" height="14" rx="1"/><circle cx="8" cy="7" r="1.5"/><path d="M6 11h4M7 3h2"/></svg></div>
  <div class="btn btn--blue" style="top:376px">CREATE ACCOUNT
    <svg viewBox="0 0 16 16"><circle cx="8" cy="8" r="7"/><circle cx="8" cy="6.5" r="2.5"/><path d="M3.5 13c1-2.5 3-3 4.5-3s3.5.5 4.5 3"/></svg></div>
  <nav class="footer"><span>Terms and Conditions</span><span>Privacy Policy</span><span>About</span><span>The Team</span></nav>
</section>

<!-- Create account -->
<section class="screen screen--signup">
  <svg class="band" viewBox="0 0 224 120" preserveAspectRatio="none">
    <defs><linearGradient id="bandB" x1="0" y1="0" x2="1" y2="1"><stop offset="0" stop-color="#4c9df0"/><stop offset=".6" stop-color="#1560c4"/><stop offset="1" stop-color="#0d4fa8"/></linearGradient></defs>
    <polygon points="0,0 224,0 224,84 144,104 0,72" fill="url(#bandB)"/>
    <polygon points="144,104 224,84 224,90" fill="#b8bcc2"/>
  </svg>
  <h1 class="wordmark band__wordmark" style="top:32px">KELPMARROW LLC</h1>
  <p class="band__sub" style="top:62px">CREATE <b>ACCOUNT</b></p>
  <span class="band__rule" style="top:79px"></span>
  <div class="field" style="top:117px">Name
    <svg viewBox="0 0 16 16"><rect x="1" y="4" width="14" height="10"/><rect x="3" y="7" width="4" height="5"/><path d="M9 8h4M9 10.5h4M7 4V2h2v2"/></svg></div>
  <div class="field" style="top:156px">Date of Birth
    <svg viewBox="0 0 16 16"><rect x="1.5" y="3" width="13" height="11.5"/><path d="M1.5 6h13M4 1.5v3M8 1.5v3M12 1.5v3"/><circle cx="8" cy="9.5" r="1.3"/></svg></div>
  <div class="field" style="top:196px">Gender
    <svg viewBox="0 0 16 16"><circle cx="5" cy="6" r="3"/><path d="M5 9v6M3 12.5h4"/><circle cx="11" cy="10.5" r="3"/><path d="M11 7.5V1M9 3l2-2 2 2"/></svg></div>
  <div class="field" style="top:235px">Email
    <svg viewBox="0 0 16 16"><path d="M1 7l7-5 7 5v8H1z"/><path d="M1 7l7 5 7-5"/><circle cx="8" cy="6" r="1.5"/></svg></div>
  <div class="field" style="top:275px">Phone
    <svg viewBox="0 0 16 16"><path d="M3 2l3 3-1.5 2c1 2 2.5 3.5 4.5 4.5L11 10l3 3-2 2C6.5 14 2 9.5 1 4z"/><path d="M10 3a3 3 0 0 1 3 3M10 1a5 5 0 0 1 5 5"/></svg></div>
  <div class="field" style="top:315px">Country
    <svg viewBox="0 0 16 16"><path d="M3 15V1.5h10l-2 3 2 3H3"/></svg></div>
  <div class="field" style="top:354px">State/ZIP or Region
    <svg viewBox="0 0 16 16"><path d="M10 1.5a3.5 3.5 0 0 1 3.5 3.5c0 2.5-3.5 6-3.5 6S6.5 7.5 6.5 5A3.5 3.5 0 0 1 10 1.5z"/><circle cx="10" cy="5" r="1.2"/><path d="M2 9l3 1.5 1-.5M2 9v5l4 1.5 4-1.5"/></svg></div>
  <div class="btn btn--blue" style="top:395px">CREATE ACCOUNT
    <svg viewBox="0 0 16 16"><circle cx="8" cy="8" r="7"/><circle cx="8" cy="6.5" r="2.5"/><path d="M3.5 13c1-2.5 3-3 4.5-3s3.5.5 4.5 3"/></svg></div>
  <nav class="footer"><span>Terms and Conditions</span><span>Privacy Policy</span><span>About</span><span>The Team</span></nav>
</section>

<!-- Weekly training challenge -->
<section class="screen screen--challenge">
  <svg class="band" viewBox="0 0 224 120" preserveAspectRatio="none">
    <defs><linearGradient id="bandC" x1="0" y1="0" x2="1" y2="1"><stop offset="0" stop-color="#4c9df0"/><stop offset=".6" stop-color="#1560c4"/><stop offset="1" stop-color="#0d4fa8"/></linearGradient></defs>
    <polygon points="0,0 224,0 224,100 130,124 0,100" fill="url(#bandC)"/>
    <polygon points="150,119 224,100 224,108" fill="#b8bcc2"/>
  </svg>
  <h1 class="wordmark band__wordmark" style="top:32px">KELPMARROW LLC</h1>
  <p class="band__sub" style="top:62px">WEEKLY <b>TRAINING CHALLENGE</b></p>
  <span class="band__rule" style="top:79px"></span>
  <div class="badge" aria-hidden="true"></div>

  <div class="week" style="left:6px;top:162px"><span class="week__ball"></span>W1</div>
  <div class="week" style="left:59px;top:162px"><span class="week__ball"></span>W2</div>
  <div class="week" style="left:111px;top:162px"><span class="week__ball"></span>W3</div>
  <div class="week" style="left:164px;top:162px"><span class="week__ball"></span>W4</div>

  <div class="week" style="left:6px;top:227px"><span class="week__ball"></span>W5</div>
  <div class="week" style="left:59px;top:227px"><span class="week__ball week__ball--green"></span>W6</div>
  <div class="week" style="left:111px;top:227px"><span class="week__ball week__ball--teal"></span>W7</div>
  <div class="week" style="left:164px;top:227px"><span class="week__ball week__ball--violet"></span>W8</div>

  <div class="week" style="left:6px;top:292px"><span class="week__ball"></span>W9</div>
  <div class="week" style="left:59px;top:292px"><span class="week__ball"></span>W10</div>
  <div class="week" style="left:111px;top:292px"><span class="week__ball"></span>W11</div>
  <div class="week" style="left:164px;top:292px"><span class="week__ball"></span>W12</div>

  <div class="week" style="left:6px;top:357px"><span class="week__ball"></span>W13</div>
  <div class="week" style="left:59px;top:357px"><span class="week__ball"></span>W14</div>
  <div class="week" style="left:111px;top:357px"><span class="week__ball"></span>W15</div>
  <div class="week" style="left:164px;top:357px"><span class="week__ball"></span>W16</div>

  <nav class="tabbar">
    <div class="tabbar__item"><svg viewBox="0 0 30 26"><path d="M2 18c5-8 12-10 18-10M4 21c5-6 11-8 16-8" fill="none" stroke="#111" stroke-width="1.3"/><circle cx="22" cy="12" r="6" fill="#fff" stroke="#111" stroke-width="1.5"/></svg></div>
    <div class="tabbar__item"><svg viewBox="0 0 30 26"><circle cx="15" cy="13" r="12" fill="#fff" stroke="#111" stroke-width="1.6"/><circle cx="15" cy="10" r="4" fill="#111"/><path d="M7 21c2-4 5-5 8-5s6 1 8 5z" fill="#111"/></svg></div>
    <div class="tabbar__item"><svg viewBox="0 0 30 26"><path d="M15 1l10 3v8c0 6-5 10-10 13C10 22 5 18 5 12V4z" fill="#fff" stroke="#111" stroke-width="1.6"/><path d="M15 4l7 2v6h-7zM15 12H8c0 4 3 8 7 10z" fill="#111"/></svg></div>
    <div class="tabbar__item"><svg viewBox="0 0 30 26"><path d="M2 14c0-3 1-5 3-5l8 2 6 4h7c2 0 3 1 3 3v2H2z" fill="#111"/><path d="M5 22v2M11 22v2M19 22v2M25 22v2" stroke="#111" stroke-width="2"/></svg></div>
  </nav>
</section>

</body>
</html>
```